Freelance yoga teacher looking for professional postcard design

I need a postcard that shows my class times & venues. I also would like it to show that I offer private one to one sessions for those not ready for group practice, or who require personal attention. It needs to show my contact details - mob: 07346218850, email & website addresses. I also want the opportunity to add other services in future, such as my website and yoga massage.

UPDATE 18 JULY

FRONT OF POSTCARD
I would like the front side of the postcard to not look too busy or 'wordy'. If using bullet points, be creative, so no ticks. Please use my full name Maren T Holloway NCM Dip.

REVERSE SIDE
The reverse side I think should have the NCM logo, together with words describing classes, 'classes are designed...' please omit the sentences starting 'by running courses...'

'Postage required' or lines for an address are not required.

Make the 'where I teach' venues/times look personable, so no harsh gridlines please.

Target Market(s)

Most of my students are 30+ professionals with disposable income or early retirees.

Industry/Entity Type

Teacher

Requirements
Must have
• It must show my National Circle of Movement Teacher Logo which I can supply.
Maren T Holloway is a National Circle of Movement trained teacher.
Classes are small and friendly, designed to create ease in the body, reduce stress and promote relaxation. Maren is passionate about sharing yoga, respecting each individual and modifying to suit their needs, leading to improved function, mobility and stability.

Keep any images simple, such as rolled up yoga mats. I am commissioning a personal mandala which I will use as a logo, but this will not be ready until mid to late August.

Please see attached 'attempt' at a postcard giving details of classes/venues, contact info.
Nice to have
• Somewhere on the postcard the words: 'Yoga. Centre the body & mind. Stretch the possibilities.'
Should not have
• Images of people doing yoga or silhouettes of yoga postures.

```html
<!DOCTYPE html>
<html lang="en">
<head>
<meta charset="utf-8">
<title>Yoga with Maren Holloway NCM Dip – Postcard Front</title>
<link rel="stylesheet" href="https://fonts.googleapis.com/css2?family=Nunito:wght@800;900&family=Didact+Gothic&family=Questrial&display=swap">
<style>
  :root {
    --page: #ffffff;
    --card: #c17f35;
    --teal: #7ccbc8;
    --tagline: #6fd0dc;
    --mandala: #5cc6e0;
    --white: #ffffff;
    --red: #bf2330;
    --orange-top: #e8652a;
    --orange-bottom: #f39524;
    --dots: rgba(236, 178, 110, 0.55);
  }
  * { margin: 0; padding: 0; box-sizing: border-box; }
  html, body {
    width: 1200px; height: 930px; overflow: hidden; background: var(--page);
  }
  .canvas { position: relative; width: 1200px; height: 930px; }
  .postcard {
    position: absolute; left: 30px; top: 30px; width: 1140px; height: 870px;
    background: var(--card); overflow: hidden;
  }
  .backdrop { position: absolute; inset: 0; width: 1140px; height: 870px; }
  .halftone {
    position: absolute; right: -120px; top: -160px; width: 780px; height: 620px;
    border-radius: 50%;
    background: radial-gradient(ellipse at 75% 30%, var(--dots) 0%, rgba(236,178,110,0.25) 45%, rgba(193,127,53,0) 70%);
  }
  .heading { position: absolute; left: 67px; top: 60px; }
  .heading-yoga {
    font-family: "Questrial", sans-serif; font-weight: 400; color: var(--teal);
    font-size: 44px; letter-spacing: 7px; -webkit-text-stroke: 1.2px var(--teal);
  }
  .heading-with {
    font-family: "Didact Gothic", sans-serif; color: var(--teal); font-size: 22px;
    margin-left: 6px;
  }
  .heading-name {
    font-family: "Nunito", sans-serif; font-weight: 900; color: var(--white);
    font-size: 62px; line-height: 1; margin-top: 6px;
    text-shadow: 2px 3px 3px rgba(80, 40, 10, 0.55);
  }
  .services { position: absolute; left: 118px; top: 362px; list-style: none; }
  .services li {
    display: flex; align-items: center; height: 42px;
    font-family: "Didact Gothic", sans-serif; font-style: italic; color: var(--white);
    font-size: 26px;
  }
  .service-mark {
    width: 42px; height: 22px; margin-right: 25px;
    background: radial-gradient(ellipse at 50% 70%, #a9d8cf 0%, #8cc7bd 60%, rgba(140,199,189,0) 72%);
  }
  .see-over {
    position: absolute; left: 413px; top: 505px;
    font-family: "Didact Gothic", sans-serif; font-style: italic; color: var(--white);
    font-size: 19px;
  }
  .mandala {
    position: absolute; left: 710px; top: 328px; width: 414px; height: 414px;
    border-radius: 50%;
    background: radial-gradient(circle, rgba(92,198,224,0.55) 0%, rgba(92,198,224,0.3) 55%, rgba(92,198,224,0.45) 100%);
  }
  .tagline {
    position: absolute; left: 28px; top: 748px;
    font-family: "Questrial", sans-serif; color: var(--tagline);
    font-size: 35px; line-height: 43px;
  }
  .tagline span { display: block; }
  .tagline .indent { padding-left: 50px; }
</style>
</head>
<body>
<main class="canvas">
  <section class="postcard">
    <div class="halftone" role="img" aria-label="Faint radiating dot pattern"></div>
    <svg class="backdrop" viewBox="0 0 1140 870" aria-hidden="true">
      <defs>
        <linearGradient id="orangeSweep" x1="0" y1="0" x2="0" y2="1">
          <stop offset="0" stop-color="var(--orange-top)"/>
          <stop offset="1" stop-color="var(--orange-bottom)"/>
        </linearGradient>
      </defs>
      <path d="M0,600 C290,585 580,700 830,810 C930,800 1040,780 1140,760 L1140,870 L0,870 Z" fill="url(#orangeSweep)"/>
      <path d="M0,560 C290,545 600,690 925,842 C620,730 320,600 0,600 Z" fill="var(--red)"/>
      <path d="M440,610 C680,700 930,800 1140,705 L1140,755 C930,835 690,735 440,610 Z" fill="var(--red)"/>
    </svg>

    <header class="heading">
      <div><span class="heading-yoga">YOGA</span><span class="heading-with">with</span></div>
      <h1 class="heading-name">Maren Holloway NCM Dip</h1>
    </header>

    <ul class="services">
      <li><span class="service-mark" role="img" aria-label="Lotus flower bullet"></span>Group classes</li>
      <li><span class="service-mark" role="img" aria-label="Lotus flower bullet"></span>Private sessions</li>
      <li><span class="service-mark" role="img" aria-label="Lotus flower bullet"></span>Therapeutic Thai Yoga Massage</li>
    </ul>
    <p class="see-over">See over for details...</p>

    <div class="mandala" role="img" aria-label="Personal mandala emblem in light blue line work"></div>

    <p class="tagline">
      <span>Centre your body and mind</span>
      <span class="indent">Stretch the possibilities</span>
    </p>
  </section>
</main>
</body>
</html>
```